We are a company specializing in African Textiles. We need a label for a new brand called BRAMHOLDEN, which is a very high quality product.
It needs to have the London skyline/silhouette and must have depth & show magnitude.
(The attached file shows images we like).
The colours need to be elegant.
The main label size is: 240 x 160mm
We will also need it in A6 size - 148 x 105mm

Target Market(s)

Customers who are looking for the finest quality fabrics & appreciate designer labels.

Industry/Entity Type

It Company

Requirements
Must have
• It must have the London skyline/Silhoutte & the details shown in the file.
• It needs to show depth & reflect the magnitude of a large BRAMHOLDEN like London.
• The fonts need to be very legible, but have character.
• The general feel must be elegant, classy & up market.
Should not have
• No tacky colours.
• The colours should reflect elegance & sophistication.

```html
<!DOCTYPE html>
<html lang="en">
<head>
<meta charset="utf-8">
<title>Bramholden Label</title>
<link href="https://fonts.googleapis.com/css2?family=Bebas+Neue&family=Cinzel:wght@400&family=Rajdhani:wght@700&family=Questrial&display=swap" rel="stylesheet">
<style>
  :root {
    --green: #22a233;
    --green-dark: #1d8a29;
    --green-deep: #145a1c;
    --stone-light: #3b3b3b;
    --stone-dark: #0f0f0f;
    --band: #000000;
  }
  html, body {
    margin: 0;
    padding: 0;
    overflow: hidden;
    background: #000;
  }
  .label {
    position: relative;
    width: 738px;
    height: 1200px;
    overflow: hidden;
    background:
      radial-gradient(ellipse at 50% 45%, var(--stone-light) 0%, #262626 45%, var(--stone-dark) 100%);
  }
  .frame {
    position: absolute;
    background: var(--green);
  }
  .frame--top { left: 24px; top: 21px; width: 691px; height: 2px; }
  .frame--upper-left { left: 23px; top: 21px; width: 2px; height: 216px; }
  .frame--upper-right { left: 713px; top: 21px; width: 2px; height: 216px; }
  .frame--lower-left { left: 23px; top: 516px; width: 2px; height: 310px; }
  .frame--lower-right { left: 711px; top: 516px; width: 2px; height: 502px; }

  .masthead {
    position: absolute;
    left: 0;
    top: 260px;
    width: 738px;
    height: 230px;
  }
  .brand-name {
    font-family: "Bebas Neue", "Arial Narrow", sans-serif;
    font-size: 196px;
    fill: var(--green);
  }
  .company-name {
    font-family: "Cinzel", "Times New Roman", serif;
    font-size: 36px;
    fill: var(--green-dark);
  }

  .specs {
    position: absolute;
    left: 0;
    top: 626px;
    width: 738px;
    margin: 0;
    text-align: center;
    font-family: "Rajdhani", "Arial", sans-serif;
    font-weight: 700;
    font-size: 44px;
    line-height: 50px;
    letter-spacing: 1px;
    color: var(--green-dark);
  }
  .specs span { display: block; }

  .skyline {
    position: absolute;
    left: 0;
    top: 856px;
    width: 738px;
    height: 256px;
    background: linear-gradient(180deg, rgba(27,122,38,0.35) 0%, var(--green-dark) 45%, var(--green-deep) 100%);
  }

  .footer-band {
    position: absolute;
    left: 0;
    top: 1112px;
    width: 738px;
    height: 88px;
    background: var(--band);
  }
  .web-address {
    margin: 0;
    padding-top: 27px;
    text-align: center;
    font-family: "Questrial", "Arial", sans-serif;
    font-size: 31px;
    letter-spacing: 1px;
    color: var(--green-dark);
  }
</style>
</head>
<body>
  <div class="label">
    <div class="frame frame--top"></div>
    <div class="frame frame--upper-left"></div>
    <div class="frame frame--upper-right"></div>
    <div class="frame frame--lower-left"></div>
    <div class="frame frame--lower-right"></div>

    <svg class="masthead" viewBox="0 0 738 230" aria-label="Bramholden, Kestrel Weavers and Co Limited">
      <text class="brand-name" x="28" y="152" textLength="692" lengthAdjust="spacingAndGlyphs">BRAMHOLDEN</text>
      <text class="company-name" x="70" y="214" textLength="616" lengthAdjust="spacingAndGlyphs">KESTREL WEAVERS &amp; CO LIMITED</text>
    </svg>

    <p class="specs">
      <span>100% EGYPTIAN COTTON</span>
      <span>MADE IN GERMANY</span>
      <span>LONDON</span>
    </p>

    <div class="skyline" role="img" aria-label="Green silhouette of the London skyline: Big Ben, the Gherkin, the London Eye, townhouses and Tower Bridge"></div>

    <div class="footer-band">
      <p class="web-address">WWW.KESTRELWEAVERS.CO.UK</p>
    </div>
  </div>
</body>
</html>
```